Webdesign für IT-Dienstleister
Zielgruppe
Seit 1997 bieten wir erstklassige IT-Dienstleistungen Mainz an, die darauf ausgerichtet sind, Unternehmen und Privatkunden mit kompetenter Beratung, zuverlässiger Unterstützung und modernen Technologielösungen zur Seite zu stehen.
Umfassende Computer-Serviceleistungen
Unser Computer-Service Mainz beinhaltet eine Reihe von Dienstleistungen, die darauf abzielen, die Leistungsfähigkeit Ihrer IT-Infrastruktur zu optimieren und zu erhalten. Von der Fehlerdiagnose bis hin zur Wartung bieten wir ein Rundum-Sorglos-Paket für Ihre Hardware und Software.
Professionelle Fehleranalyse und Reparatur
Optimierung von Betriebssystemen und Anwendungen
Regelmäßige Wartungsarbeiten zur Vorbeugung von Ausfällen
Ersetzen und Aufrüsten von Hardware-Komponenten
Aufgabenstellung
Ich hätte gern ein modernes Design. Ein Logo vorhanden, sollte mit eingebaut werden.
Ansonsten hätte ich gerne eine einzelne Webseite mit den Firmen Infos (und den Links zu Sozial Media) und einer extra Impressum Seite. Und wenn möglich noch ein Anfrage Formular.
Am liebsten wäre ein Format welches ich in WordPress verarbeiten werden kann.
(Logo wird noch nachgereicht)

```html
<!DOCTYPE html>
<html lang="de">
<head>
<meta charset="utf-8">
<title>Kontakt – rechner-werk.de</title>
<link rel="stylesheet" href="https://fonts.googleapis.com/css2?family=Poppins:wght@400;500&display=swap">
<style>
:root{
  --blue:#14a3d6;
  --navy:#12214a;
  --ink:#1b1f2b;
  --white:#ffffff;
  --line:#c9d3dc;
  --muted:#8a93a8;
}
*{margin:0;padding:0;box-sizing:border-box}
html,body{width:1200px;height:1024px;overflow:hidden}
body{font-family:'Poppins',sans-serif;color:var(--ink);background:var(--white);position:relative}
.abs{position:absolute}
a{color:inherit;text-decoration:none}

/* header */
.site-header{left:0;top:0;width:1200px;height:81px;background:var(--white)}
.brand{display:flex;align-items:center;gap:8px}
.brand-mark{width:30px;height:30px;border-radius:50%;border:3px solid var(--blue)}
.brand-name{font-size:20px;font-weight:500;color:var(--blue);letter-spacing:-.2px}
.site-header .brand{left:173px;top:25px}
.topbar{left:669px;top:0;width:358px;height:25px;background:var(--blue);border-radius:0 0 3px 3px;display:flex;align-items:center;justify-content:center;gap:14px;color:var(--white);font-size:8.5px}
.topbar span{display:flex;align-items:center;gap:4px}
.nav{top:44px;font-size:10.5px;font-weight:500;color:var(--ink)}
.nav.active{color:var(--blue);border-bottom:1px solid var(--blue);padding-bottom:2px}
.pill{display:flex;align-items:center}
.pill-label{border:1px solid var(--ink);border-radius:14px;height:26px;display:flex;align-items:center;padding:0 14px;font-size:10.5px;font-weight:500;color:var(--ink);background:var(--white)}
.pill-arrow{width:26px;height:26px;border:1px solid var(--ink);border-radius:50%;display:flex;align-items:center;justify-content:center;background:var(--white)}

/* hero */
.hero{left:0;top:81px;width:1200px;height:714px;background:var(--blue)}
.eyebrow{left:0;top:139px;width:1200px;text-align:center;color:var(--white);font-size:9.5px;letter-spacing:1.5px}
.hero-title{left:0;top:151px;width:1200px;text-align:center;color:var(--white);font-size:30px;font-weight:500}

/* card */
.contact-card{left:173px;top:231px;width:854px;height:365px;background:var(--white);border-radius:12px;overflow:hidden}
.company{left:39px;top:36px;font-size:16px;font-weight:500;color:var(--blue)}
.address{left:39px;top:64px;font-size:10px;line-height:17.5px}
.channel{left:39px;display:flex;align-items:center;font-size:10px}
.channel svg{margin-right:6px}
.channel b{font-weight:500;width:46px}
.portrait{left:121px;top:56px;width:275px;height:309px;background:linear-gradient(160deg,#dfe6ee 0%,#c9d5e3 55%,#b7c5d6 100%);border-radius:120px 120px 0 0}
.form-title{left:427px;top:36px;font-size:16px;font-weight:500}
.form-intro{left:427px;top:64px;font-size:10px}
.field{border:1px solid var(--line);border-radius:2px;color:var(--blue);font-size:10px;padding:0 12px;display:flex;align-items:center}
.field.area{align-items:flex-start;padding-top:11px}
.consent{left:427px;top:303px;display:flex;gap:7px;font-size:8.5px;line-height:12.5px}
.check{width:12px;height:12px;border-radius:3px;background:var(--blue);display:flex;align-items:center;justify-content:center;margin-top:1px}
.consent u{font-weight:500}

/* newsletter */
.nl-title{left:0;top:678px;width:1200px;text-align:center;color:var(--white);font-size:16px;font-weight:500}
.nl-text{left:0;top:709px;width:1200px;text-align:center;color:var(--white);font-size:11px;font-weight:500;line-height:17.5px}
.nl-form{left:381px;top:772px;width:438px;height:47px;background:var(--white);border-radius:24px;z-index:2}
.nl-input{left:21px;top:16px;font-size:10px;color:var(--blue)}
.nl-form .pill{right:9px;top:10px}

/* footer */
.site-footer{left:0;top:795px;width:1200px;height:229px;background:var(--navy)}
.site-footer .brand{left:173px;top:104px}
.site-footer .brand-name{color:var(--white)}
.site-footer .brand-mark{border-color:var(--white)}
.follow{left:729px;top:125px;color:var(--white);font-size:10.5px;font-weight:500}
.socials{left:901px;top:119px;display:flex;gap:6px}
.social{width:27px;height:27px;border-radius:50%;background:var(--white)}
.rule{left:173px;top:167px;width:854px;height:1px;background:rgba(255,255,255,.15)}
.copyright{left:173px;top:183px;color:var(--muted);font-size:10.5px}
.legal{right:173px;top:183px;display:flex;gap:22px;color:var(--white);font-size:10.5px;font-weight:500}
</style>
</head>
<body>

<header class="site-header abs">
  <div class="brand abs"><span class="brand-mark"></span><span class="brand-name">rechner-werk.de</span></div>
  <div class="topbar abs">
    <span><svg width="11" height="11" viewBox="0 0 24 24" fill="none" stroke="#fff" stroke-width="2"><circle cx="12" cy="12" r="10"/><path d="M8 7l2 3-1 1a6 6 0 004 4l1-1 3 2-1 2c-5 0-10-5-10-10z"/></svg>+49 (0) 6131. 55 20 410</span>
    <span><svg width="12" height="9" viewBox="0 0 24 18" fill="none" stroke="#fff" stroke-width="2"><rect x="4" y="2" width="18" height="14"/><path d="M4 2l9 8 9-8"/></svg>anfrage@rechner-werk.de</span>
    <span><svg width="11" height="11" viewBox="0 0 24 24" fill="none" stroke="#fff" stroke-width="2"><rect x="3" y="3" width="15" height="18"/><path d="M6 8h9M6 12h9M6 16h9M21 7v14"/></svg>Newsletter</span>
  </div>
  <a class="nav abs" style="left:502px">Service &amp; Wartung</a>
  <a class="nav abs" style="left:627px">DSL &amp; Internet</a>
  <a class="nav abs" style="left:729px">PC &amp; Server</a>
  <a class="nav abs active" style="left:819px">Kontakt</a>
  <div class="pill abs" style="left:892px;top:40px">
    <span class="pill-label">Anfrage senden</span>
    <span class="pill-arrow"><svg width="10" height="10" viewBox="0 0 10 10" fill="none" stroke="#1b1f2b" stroke-width="1.2"><path d="M2 8L8 2M3 2h5v5"/></svg></span>
  </div>
</header>

<section class="hero abs"></section>
<p class="eyebrow abs">KONTAKT</p>
<h1 class="hero-title abs">Der direkte Draht zu uns</h1>

<div class="contact-card abs">
  <div class="portrait abs" role="img" aria-label="Foto: lächelnder Mitarbeiter mit Tablet in hellblauem Hemd"></div>
  <h2 class="company abs">IT Dienstleistungen Brenner</h2>
  <p class="address abs">Lindenhofweg 22<br>55122 Mainz, Deutschland</p>
  <div class="channel abs" style="top:117px"><svg width="14" height="14" viewBox="0 0 24 24" fill="none" stroke="#1b1f2b" stroke-width="1.5"><circle cx="12" cy="12" r="10"/><path d="M8 7l2 3-1 1a6 6 0 004 4l1-1 3 2-1 2c-5 0-10-5-10-10z"/></svg><b>Telefon</b>+49 [0] 6131. 55 20 410</div>
  <div class="channel abs" style="top:141px"><svg width="14" height="14" viewBox="0 0 24 24" fill="none" stroke="#1b1f2b" stroke-width="1.5"><rect x="6" y="3" width="12" height="6"/><rect x="3" y="9" width="18" height="8" rx="1"/><rect x="7" y="14" width="10" height="7"/></svg><b>Telefax</b>+49 [0] 6131 55 20 411</div>
  <div class="channel abs" style="top:165px"><svg width="14" height="14" viewBox="0 0 24 18" fill="none" stroke="#1b1f2b" stroke-width="1.5"><rect x="6" y="2" width="17" height="14"/><path d="M6 2l8.5 8 8.5-8M0 6h4M1 9h3"/></svg><b>E-Mail</b>info@brenner-it.eu</div>

  <h2 class="form-title abs">Kontaktformular</h2>
  <p class="form-intro abs">Um mit uns in Kontakt zu treten, füllen Sie bitte einfach folgende Felder aus:</p>
  <div class="field abs" style="left:427px;top:106px;width:189px;height:37px">Ihr Vorname*</div>
  <div class="field abs" style="left:643px;top:106px;width:189px;height:37px">Ihr Nachname*</div>
  <div class="field abs" style="left:427px;top:155px;width:405px;height:37px">Ihre E-Mail-Adresse*</div>
  <div class="field area abs" style="left:427px;top:204px;width:405px;height:83px">Ihre Mitteilung an uns*</div>
  <div class="consent abs">
    <span class="check"><svg width="8" height="8" viewBox="0 0 10 10" fill="none" stroke="#fff" stroke-width="1.6"><path d="M1.5 5.2l2.3 2.3 4.7-5"/></svg></span>
    <span>Ich habe die <u>Datenschutzerklärung</u> gelesen<br>und akzeptiere diese hiermit.</span>
  </div>
  <div class="pill abs" style="left:727px;top:303px">
    <span class="pill-label">Absenden</span>
    <span class="pill-arrow"><svg width="10" height="10" viewBox="0 0 10 10" fill="none" stroke="#1b1f2b" stroke-width="1.2"><path d="M2 8L8 2M3 2h5v5"/></svg></span>
  </div>
</div>

<h2 class="nl-title abs">Newsletter abonnieren</h2>
<p class="nl-text abs">Verpassen Sie keine aktuellen Angebote und Neuigkeiten aus unserem Hause<br>und abonnieren unseren unverbindlichen Newsletter.</p>
<div class="nl-form abs">
  <span class="nl-input abs">Ihre E-Mail-Adresse*</span>
  <div class="pill abs">
    <span class="pill-label">Newsletter abonnieren</span>
    <span class="pill-arrow"><svg width="10" height="10" viewBox="0 0 10 10" fill="none" stroke="#1b1f2b" stroke-width="1.2"><path d="M2 8L8 2M3 2h5v5"/></svg></span>
  </div>
</div>

<footer class="site-footer abs">
  <div class="brand abs"><span class="brand-mark"></span><span class="brand-name">rechner-werk.de</span></div>
  <p class="follow abs">Folgen Sie uns bei Social Media</p>
  <div class="socials abs">
    <span class="social" aria-label="Social-Media-Profil 1"></span>
    <span class="social" aria-label="Social-Media-Profil 2"></span>
    <span class="social" aria-label="Social-Media-Profil 3"></span>
    <span class="social" aria-label="Social-Media-Profil 4"></span>
  </div>
  <div class="rule abs"></div>
  <p class="copyright abs">© 2025 IT-Dienstleistungen Brenner. All rights reserved.</p>
  <nav class="legal abs"><a>Impressum</a><a>Datenschutzerklärung</a><a>Kontakt</a></nav>
</footer>

</body>
</html>
```